Business Card Design

I require the design of business cards using my exisiting logo.

It is essential that the designer has experience with various print processes (foil stamping etc) and different paper stock.

The design is to blend in with current packaging and display unit. (Images will be provided).
A swing tag and certificate of authenticity design will als be required at a later stage.

Details which need to be included on the card are:
- Contact Name
- Position in Company
- Address
- Contact Number
- Email Address
- Web Address

Ideally I would prefer the background (both sides) to be greyish colour (offset printing or if you can suggest greyish paperstock) with silver foiling on the front and either black or metallic silver on the back.

Or another option would be grey background on the front and either white or black on the the back.

* The business card can be portrait or landscape.

Printers specifications:
Bleed 3mm
Trim Marks
Seperate file for foil printing

This task is for someone who is creative and enjoys working with fashion and luxury items!
_______________________________________________

I will require business cards designs for 2 different business and would hope to work with the same designer.

Please note I had asked for a grey colour at least on one of the sides. However I keep on getting black and white designs.   

Industry/Entity Type

Business

Requirements
Must have
• - Double sided business card
- Luxury feel
- Foil Print Priniting

- Would prefer at least grey background at least on one side of the card.

- The business card can be portrait or landscape.
Nice to have
• *The business card can be portrait or landscape.
Should not have
• - Bright Colours
- Alterations to logo

```html
<!DOCTYPE html>
<html lang="en">
<head>
<meta charset="utf-8">
<title>Kestriva Gems – Business Card</title>
<link href="https://fonts.googleapis.com/css2?family=Roboto:wght@100;300;400&display=swap" rel="stylesheet">
<style>
  :root {
    --stage: #1c1c1c;
    --card-light: #ececec;
    --card-dark: #0d0d0d;
    --ink: #1a1a1a;
    --ink-soft: #3a3a3a;
    --foil: #d6d6d6;
  }
  * { margin: 0; padding: 0; box-sizing: border-box; }
  html, body { width: 1200px; height: 760px; overflow: hidden; }
  body {
    background: var(--stage);
    font-family: "Roboto", Arial, sans-serif;
    display: flex;
    align-items: center;
    justify-content: center;
    gap: 40px;
  }
  .card {
    width: 530px;
    height: 303px;
    position: relative;
    flex: none;
    overflow: hidden;
  }
  .card--front {
    background: var(--card-light);
    color: var(--ink);
  }
  .card--back {
    background: var(--card-dark);
    display: flex;
    align-items: center;
    justify-content: center;
  }
  .brand-name {
    position: absolute;
    left: 34px;
    top: 0;
    bottom: 0;
    width: 210px;
    display: flex;
    align-items: center;
    justify-content: center;
    font-weight: 300;
    font-size: 22px;
    letter-spacing: 3px;
    color: var(--ink);
    text-align: center;
    line-height: 1.3;
  }
  .contact {
    position: absolute;
    left: 268px;
    top: 62px;
    font-weight: 300;
  }
  .contact__name { font-size: 25px; font-weight: 300; letter-spacing: -0.3px; }
  .contact__role { font-size: 14px; margin: 2px 0 0 16px; color: var(--ink-soft); }
  .contact__lines { list-style: none; margin: 18px 0 0 28px; font-size: 14px; line-height: 19px; }
  .contact__lines li { display: flex; align-items: center; gap: 8px; white-space: nowrap; }
  .contact__lines svg { width: 14px; height: 12px; flex: none; }
  .contact__address { margin: 16px 0 0 50px; font-size: 14px; line-height: 19px; color: var(--ink-soft); white-space: nowrap; }
  .back-wordmark {
    font-weight: 100;
    font-size: 54px;
    letter-spacing: 2px;
    color: var(--foil);
    white-space: nowrap;
  }
</style>
</head>
<body>
  <section class="card card--front">
    <div class="brand-name">KESTRIVA<br>GEMS</div>
    <div class="contact">
      <p class="contact__name">Name Surname</p>
      <p class="contact__role">Manager</p>
      <ul class="contact__lines">
        <li>
          <svg viewBox="0 0 14 12" aria-hidden="true"><rect x="1" y="3" width="12" height="8" fill="none" stroke="#1a1a1a" stroke-width="1.2"/><rect x="3" y="1" width="8" height="2.5" fill="none" stroke="#1a1a1a" stroke-width="1.2"/><rect x="4" y="5.5" width="6" height="3.5" fill="#1a1a1a"/></svg>
          <span>(221) 30 412 76 54</span>
        </li>
        <li>
          <svg viewBox="0 0 14 12" aria-hidden="true"><rect x="1" y="1.5" width="12" height="9" fill="none" stroke="#1a1a1a" stroke-width="1.2"/><path d="M1 1.5 L13 10.5 M13 1.5 L1 10.5" stroke="#1a1a1a" stroke-width="1.2"/></svg>
          <span>name@kestriva-gems.com</span>
        </li>
      </ul>
      <p class="contact__address">Rue des Lilas - Mont Clair<br>BP 218 - City, Country<br>www.kestriva-gems.com</p>
    </div>
  </section>
  <section class="card card--back">
    <p class="back-wordmark">KESTRIVA GEMS</p>
  </section>
</body>
</html>
```